Kalmoret Windham & Associates

We would like a simple, professional business card using a similar font to our logo.

Industry/Entity Type

Law Firm

Contact Information for Business Card

Martin Kalmoret, Esq. 47 Tillman Lane, 2nd Floor Hollisford, MA 02094 Office: 781.555.0143 Cell: 508.555.0196 Email: marty@kwfirmma.com kalmoretwindhamlaw.com

Font styles to use
Other font styles liked:
• We would like to use the fonts used in the logo or similar

Colors
0054AA
0677BA
7BADD7
CADEEF
E8F1F8

Requirements
Must have
• We would like the fonts to match the logo
Nice to have
• not too much design- very simple and professional business card. I added a picture of a business card that I tried to start but I am not a designer! Hopefully it will help with the address and phone numbers and kind of what we are looking for.

```html
<!DOCTYPE html>
<html lang="en">
<head>
<meta charset="utf-8">
<title>Kalmoret Windham &amp; Associates — Business Card</title>
<link rel="stylesheet" href="https://fonts.googleapis.com/css2?family=Cardo:wght@400;700&family=EB+Garamond:wght@400&family=Roboto:wght@300&display=swap">
<style>
  :root {
    --navy: #203871;
    --paper: #ffffff;
    --canvas: #f7f7f7;
    --rule: #6b6b6b;
    --ink-light: #ffffff;
  }
  * { box-sizing: border-box; margin: 0; padding: 0; }
  html, body {
    width: 800px; height: 1200px; overflow: hidden;
    background: var(--canvas);
  }
  .sheet { position: relative; width: 800px; height: 1200px; }
  .card {
    position: absolute; left: 80px; width: 640px; height: 366px;
    background: var(--paper);
    box-shadow: 0 4px 14px rgba(0,0,0,0.18);
    overflow: hidden;
  }
  .card--front { top: 204px; }
  .card--back { top: 630px; }

  /* firm lockup: plain square + rule + name */
  .lockup { display: flex; align-items: center; justify-content: center; }
  .lockup__square { background: var(--navy); flex: none; }
  .lockup__rule { background: var(--rule); width: 2px; flex: none; }
  .lockup__name {
    font-family: 'Cardo', serif; font-weight: 700;
    color: var(--navy); text-transform: uppercase;
    line-height: 0.95; letter-spacing: 0.02em;
  }

  .card--front .lockup { height: 133px; gap: 12px; }
  .card--front .lockup__square { width: 120px; height: 66px; }
  .card--front .lockup__rule { height: 92px; }
  .card--front .lockup__name { font-size: 19px; }

  .card--back .lockup { height: 366px; gap: 20px; }
  .card--back .lockup__square { width: 206px; height: 112px; }
  .card--back .lockup__rule { height: 156px; }
  .card--back .lockup__name { font-size: 33px; }

  .band {
    position: absolute; left: 0; top: 133px; width: 100%; height: 233px;
    background: var(--navy); color: var(--ink-light);
  }
  .band__name {
    position: absolute; top: 18px; width: 100%; text-align: center;
    font-family: 'EB Garamond', serif; font-size: 35px; font-weight: 400;
  }
  .contact {
    position: absolute; top: 82px;
    font-family: 'Roboto', sans-serif; font-weight: 300; font-size: 17px;
    line-height: 28px;
  }
  .contact--left { left: 74px; }
  .contact--right { left: 390px; }
  .contact__row { display: flex; align-items: flex-start; gap: 12px; }
  .contact__icon { width: 12px; height: 28px; flex: none; }
  .band__divider {
    position: absolute; left: 319px; top: 90px; width: 1px; height: 70px;
    background: var(--ink-light);
  }
  .band__web {
    position: absolute; top: 183px; width: 100%; text-align: center;
    font-family: 'EB Garamond', serif; font-size: 19px;
  }
</style>
</head>
<body>
<main class="sheet">

  <section class="card card--front" aria-label="Business card front">
    <div class="lockup">
      <span class="lockup__square"></span>
      <span class="lockup__rule"></span>
      <span class="lockup__name">Kalmoret<br>Windham<br>&amp; Associates</span>
    </div>
    <div class="band">
      <h1 class="band__name">Martin Kalmoret, Esq.</h1>

      <div class="contact contact--left">
        <div class="contact__row">
          <svg class="contact__icon" viewBox="0 0 12 28" aria-hidden="true">
            <path d="M2.5 8c-1 1-1 2.5 0 5s3 5 5 6.5c1 .7 2 .5 2.8-.3l.7-.8-2.2-2-1 .8c-1.2-.6-2.6-2.6-3-4l.9-.9-1.5-2.6z" fill="currentColor"/>
          </svg>
          <span>781.555.0143</span>
        </div>
        <div class="contact__row">
          <svg class="contact__icon" viewBox="0 0 12 28" aria-hidden="true">
            <rect x="2.5" y="8" width="7" height="12" rx="1" fill="none" stroke="currentColor" stroke-width="1.4"/>
            <rect x="5" y="17.2" width="2" height="1.2" fill="currentColor"/>
          </svg>
          <span>508.555.0196</span>
        </div>
        <div class="contact__row">
          <svg class="contact__icon" viewBox="0 0 12 28" aria-hidden="true">
            <rect x="0.5" y="11" width="11" height="7.5" fill="currentColor"/>
            <path d="M0.5 11l5.5 4 5.5-4" fill="none" stroke="#203871" stroke-width="1"/>
          </svg>
          <span>marty@kwfirmma.com</span>
        </div>
      </div>

      <span class="band__divider"></span>

      <div class="contact contact--right">
        <div class="contact__row">
          <svg class="contact__icon" viewBox="0 0 12 28" aria-hidden="true">
            <path d="M6 7.5a4 4 0 0 0-4 4c0 3 4 8 4 8s4-5 4-8a4 4 0 0 0-4-4zm0 5.6a1.6 1.6 0 1 1 0-3.2 1.6 1.6 0 0 1 0 3.2z" fill="currentColor"/>
          </svg>
          <span>47 Tillman Lane,<br>2nd Floor, Hollisford<br>MA 02094</span>
        </div>
      </div>

      <p class="band__web">kalmoretwindhamlaw.com</p>
    </div>
  </section>

  <section class="card card--back" aria-label="Business card back">
    <div class="lockup">
      <span class="lockup__square"></span>
      <span class="lockup__rule"></span>
      <span class="lockup__name">Kalmoret<br>Windham<br>&amp; Associates</span>
    </div>
  </section>

</main>
</body>
</html>
```